Create our new Brightcup Coffee Syrup Label designs. A delicious job!

Design a front label for a range of coffee syrup flavours. The brand is 'Brightcup Coffee Syrups'. The flavours, vanilla, hazelnut and caramel.
Our coffee syrups are made with only natural colours and flavours and are positioned in the popular premium space in Australian and international cafes.
The labels will be applied to 750 ml Boston Bottles (see attached image).
Given that coffee syrups are often positioned in high visibility locations in cafes, they can be considered as objects of functional beauty.
This range is a sub brand for our company and I have attached our main brand images in the flavours we want. we want this brand to look different to this Marlowe branded range, but included the image to show what we are currently doing in this space.
The different flavours can be identified by a combination of colour and text, which may be a line or section of the otherwise same overall design.
We are going to do a 2 part label with the front just carrying Brand and flavour descriptors plus 750 ml.
Total Bottle height is 240 mm bottle width is 70 mm

Target Market(s)

Cafe patrons, primarily women, 18-35, Middle class in terms of economics, regular cafe patrons. Who are looking for a guilt free treat in their busy day.

Logo Text

Brightcup Coffee Syrups Vanilla (or Hazelnut, or Caramel) 750 ml

Logo styles of interest
Pictorial/Combination Logo
Font styles to use
Sans Serif

Colors

Designer to choose colors to be used in the design.

Requirements
Must have
• A clear design, which is a combination of font and image. it needs to be legible from up to 2m away (across a counter in a cafe).
• We would like to see a device, which may be a gold drop, that may be the 'brightcup' meant to the coffee.
• The way our coffee syrups are used is by adding a small amount (15 ml) to a cup
• of coffee, this adds both flavour and sweetness to the overall coffee experience, and cafes charge a premium for this service. We want our package to show this will be a great thing to do.
• We have a few options in terms of Label stock. We can print on a foil, that will allow a metallic sheen to come through the colours (see example of the Marlowe branded bottles.
Nice to have
• We are looking for a modern, clean and distinctive look and feel to this range.
• I have added a key line for the front and back label, however we can create a different label die line should the design warrant that. Note this is just for the front label.
Should not have
• Difficult to read fonts or imagery that is not clear.
• Should look different to the Marlowe branded product range.

```html
<!DOCTYPE html>
<html lang="en">
<head>
<meta charset="utf-8">
<title>Brightcup Coffee Syrup – Front Labels</title>
<link rel="stylesheet" href="https://fonts.googleapis.com/css2?family=Amatic+SC:wght@400;700&family=Baloo+2:wght@700&family=Montserrat:wght@400&display=swap">
<style>
  :root {
    --paper: #ffffff;
    --gold-light: #f9c97c;
    --gold-mid: #dc9048;
    --gold-deep: #c2662a;
    --brand-orange: #dc5a26;
    --caramel: #de6424;
    --vanilla: #ea4523;
    --hazelnut: #5e4499;
    --cream: #e9d5c3;
    --cocoa: #6a4b36;
    --rule: #eabf9c;
  }
  * { margin: 0; padding: 0; box-sizing: border-box; }
  html, body { width: 1200px; height: 849px; overflow: hidden; background: var(--paper); }
  .sheet { position: relative; width: 1200px; height: 849px; }

  .label { position: absolute; top: 40px; width: 368px; height: 725px; overflow: hidden; }
  .label--caramel { left: 29px; }
  .label--vanilla { left: 416px; }
  .label--hazelnut { left: 820px; }

  .drip-top, .drip-bottom { position: absolute; left: 0; width: 100%; }
  .drip-top {
    top: 0; height: 96px;
    background: linear-gradient(90deg, var(--gold-light), var(--gold-mid) 35%, var(--gold-deep) 60%);
    border-radius: 0 0 40px 40px;
  }
  .drip-bottom {
    bottom: 0; height: 130px;
    background: linear-gradient(90deg, var(--gold-deep) 40%, var(--gold-mid) 70%, var(--gold-light));
    border-radius: 40px 40px 0 0;
  }

  .brand { position: absolute; top: 112px; left: 0; width: 100%; text-align: center; }
  .brand__dot { display: block; width: 34px; height: 34px; margin: 0 auto 16px; border-radius: 50%; background: var(--brand-orange); }
  .brand__name { font-family: 'Baloo 2', sans-serif; font-weight: 700; font-size: 14px; letter-spacing: 0.6px; color: var(--brand-orange); }

  .panel {
    position: absolute; top: 265px; left: 13px; width: 332px; height: 337px;
    border-radius: 20px;
  }
  .label--caramel .panel { background: var(--caramel); }
  .label--vanilla .panel { background: var(--vanilla); }
  .label--hazelnut .panel { background: var(--hazelnut); }

  .panel__rule { position: absolute; height: 3px; border-radius: 2px; background: var(--rule); }
  .panel__rule--top { top: 56px; left: 93px; width: 130px; }
  .panel__rule--under { top: 290px; left: 108px; width: 130px; }

  .flavour {
    position: absolute; top: 110px; left: 0; width: 100%; text-align: center;
    font-family: 'Amatic SC', sans-serif; font-weight: 700; font-size: 108px; line-height: 1;
    color: var(--cream); text-shadow: -4px 2px 0 var(--cocoa); letter-spacing: 2px;
  }
  .syrup {
    position: absolute; top: 238px; left: 0; width: 100%; text-align: center;
    font-family: 'Amatic SC', sans-serif; font-weight: 700; font-size: 42px; line-height: 1;
    color: var(--cream); text-shadow: -2px 1px 0 var(--cocoa);
  }
  .syrup::before, .syrup::after { content: "•"; padding: 0 4px; }
  .dose {
    position: absolute; top: 304px; left: 120px;
    font-family: 'Montserrat', sans-serif; font-size: 12px; color: var(--cocoa);
  }
  .label--hazelnut .dose { color: var(--cream); }
  .volume {
    position: absolute; top: 292px; right: 8px;
    font-family: 'Amatic SC', sans-serif; font-size: 32px; color: var(--rule);
  }

  .badge {
    position: absolute; left: 270px; width: 88px; height: 88px; border-radius: 50%;
    background: var(--cocoa);
    border: 6px solid var(--gold-mid);
    box-shadow: inset 0 0 0 1px var(--gold-light);
    display: flex; align-items: center; justify-content: center; text-align: center;
    font-family: 'Amatic SC', sans-serif; font-weight: 400; font-size: 21px; line-height: 1.05;
    color: var(--gold-light);
  }
  .badge--flavours { top: 204px; }
  .badge--colours { top: 300px; }

  .origin {
    position: absolute; top: 606px; left: 0; width: 100%; text-align: center;
    font-family: 'Amatic SC', sans-serif; font-size: 25px; letter-spacing: 1px; color: var(--cocoa);
  }
</style>
</head>
<body>
<main class="sheet">

  <section class="label label--caramel">
    <div class="drip-top" role="img" aria-label="Golden caramel drips running down from the top edge"></div>
    <div class="drip-bottom" role="img" aria-label="Golden caramel pool rising at the bottom edge"></div>
    <div class="brand"><span class="brand__dot"></span><span class="brand__name">Brightcup Coffee Syrup</span></div>
    <div class="panel">
      <span class="panel__rule panel__rule--top"></span>
      <h2 class="flavour">CARAMEL</h2>
      <p class="syrup">SYRUP</p>
      <span class="panel__rule panel__rule--under"></span>
      <p class="dose">15ml/cup of coffee</p>
      <p class="volume">750ML</p>
    </div>
    <div class="badge badge--flavours">NATURAL<br>FALVORS</div>
    <div class="badge badge--colours">NATURAL<br>COLOURS</div>
    <p class="origin">AUSTRALIAN MADE AND OWNED</p>
  </section>

  <section class="label label--vanilla">
    <div class="drip-top" role="img" aria-label="Golden caramel drips running down from the top edge"></div>
    <div class="drip-bottom" role="img" aria-label="Golden caramel pool rising at the bottom edge"></div>
    <div class="brand"><span class="brand__dot"></span><span class="brand__name">Brightcup Coffee Syrup</span></div>
    <div class="panel">
      <span class="panel__rule panel__rule--top"></span>
      <h2 class="flavour">VANILLA</h2>
      <p class="syrup">SYRUP</p>
      <span class="panel__rule panel__rule--under"></span>
      <p class="dose">15ml/cup of coffee</p>
      <p class="volume">750ML</p>
    </div>
    <div class="badge badge--flavours">NATURAL<br>FALVORS</div>
    <div class="badge badge--colours">NATURAL<br>COLOURS</div>
    <p class="origin">AUSTRALIAN MADE AND OWNED</p>
  </section>

  <section class="label label--hazelnut">
    <div class="drip-top" role="img" aria-label="Golden caramel drips running down from the top edge"></div>
    <div class="drip-bottom" role="img" aria-label="Golden caramel pool rising at the bottom edge"></div>
    <div class="brand"><span class="brand__dot"></span><span class="brand__name">Brightcup Coffee Syrup</span></div>
    <div class="panel">
      <span class="panel__rule panel__rule--top"></span>
      <h2 class="flavour">HAZELNUT</h2>
      <p class="syrup">SYRUP</p>
      <span class="panel__rule panel__rule--under"></span>
      <p class="dose">15ml/cup of coffee</p>
      <p class="volume">750ML</p>
    </div>
    <div class="badge badge--flavours">NATURAL<br>FALVORS</div>
    <div class="badge badge--colours">NATURAL<br>COLOURS</div>
    <p class="origin">AUSTRALIAN MADE AND OWNED</p>
  </section>

</main>
</body>
</html>
```